Women's Health Company needs business card

We need a business card for a USA based women's health care company. We use digital technology to enhance therapy prescribed by clinicians for their patients

```html
<!DOCTYPE html>
<html lang="en">
<head>
<meta charset="utf-8">
<title>Velora Health – Business Card</title>
<link href="https://fonts.googleapis.com/css2?family=Roboto:wght@300;400;700&display=swap" rel="stylesheet">
<style>
  :root {
    --purple: #7e4a93;
    --purple-front: #8a539b;
    --teal: #6cb8b2;
    --white: #f7f6f6;
    --backdrop: #e4e3e6;
    --ink-light: #ffffff;
  }
  * { margin: 0; padding: 0; box-sizing: border-box; }
  html, body {
    width: 1200px; height: 874px; overflow: hidden;
    background: var(--backdrop);
    font-family: "Roboto", Arial, sans-serif;
  }
  .sheet {
    width: 1200px; height: 874px;
    display: flex; flex-direction: column; align-items: center; justify-content: center;
    gap: 30px;
  }
  .card {
    position: relative;
    width: 700px; height: 400px;
    border-radius: 22px;
    overflow: hidden;
    box-shadow: 0 6px 18px rgba(0,0,0,0.15);
  }
  .card-front {
    background: var(--purple-front);
    display: flex; align-items: center; justify-content: center;
  }
  .wordmark {
    font-weight: 300;
    color: var(--teal);
    letter-spacing: 0.02em;
    white-space: nowrap;
  }
  .card-front .wordmark { font-size: 72px; }
  .card-back { background: var(--white); }
  .card-back .wave { position: absolute; inset: 0; width: 100%; height: 100%; }
  .card-back .wordmark {
    position: absolute; left: 36px; top: 34px;
    font-size: 30px;
  }
  .contact {
    position: absolute; right: 48px; bottom: 24px;
    text-align: right; color: var(--ink-light);
  }
  .contact-name { font-size: 23px; font-weight: 700; line-height: 1.1; }
  .contact-title { font-size: 14px; font-weight: 400; line-height: 1.3; margin-bottom: 10px; }
  .contact-address { font-size: 14px; line-height: 1.3; margin-bottom: 10px; }
  .contact-lines { list-style: none; font-size: 14px; line-height: 1.35; }
  .contact-lines li { display: flex; justify-content: flex-end; align-items: center; gap: 8px; }
  .contact-lines svg { width: 13px; height: 13px; fill: var(--ink-light); flex: none; }
</style>
</head>
<body>
<main class="sheet">
  <section class="card card-front" aria-label="Card front">
    <span class="wordmark">Velora Health</span>
  </section>

  <section class="card card-back" aria-label="Card back">
    <svg class="wave" viewBox="0 0 700 400" preserveAspectRatio="none" aria-hidden="true">
      <path d="M118 400 C 300 280, 460 140, 700 146 L700 400 Z" fill="var(--teal)"/>
      <path d="M140 400 C 316 292, 472 160, 700 164 L700 400 Z" fill="var(--purple)"/>
    </svg>
    <span class="wordmark">Velora Health</span>
    <div class="contact">
      <p class="contact-name">Daniel Moore</p>
      <p class="contact-title">Managing Director</p>
      <p class="contact-address">4120 Maple Court<br>Portland, Oregon 97205</p>
      <ul class="contact-lines">
        <li>555-214-7730
          <svg viewBox="0 0 24 24"><path d="M6.6 10.8a15.1 15.1 0 0 0 6.6 6.6l2.2-2.2a1 1 0 0 1 1-.25 11.4 11.4 0 0 0 3.6.57 1 1 0 0 1 1 1V20a1 1 0 0 1-1 1A17 17 0 0 1 3 4a1 1 0 0 1 1-1h3.5a1 1 0 0 1 1 1c0 1.25.2 2.45.57 3.570a1 1 0 0 1-.25 1z"/></svg>
        </li>
        <li>555-386-1942
          <svg viewBox="0 0 24 24"><path d="M7 1h10a2 2 0 0 1 2 2v18a2 2 0 0 1-2 2H7a2 2 0 0 1-2-2V3a2 2 0 0 1 2-2zm0 3v15h10V4z"/></svg>
        </li>
        <li>info@velorahealth.com
          <svg viewBox="0 0 24 24"><path d="M2 5h20v14H2zm2 2v.5l8 5 8-5V7zm0 2.8V17h16V9.8l-8 5z"/></svg>
        </li>
        <li>www.velorahealth.com
          <svg viewBox="0 0 24 24"><path d="M12 2a10 10 0 1 0 0 20 10 10 0 0 0 0-20zm-1 17.9A8 8 0 0 1 4.2 10L9 14.8v1a2 2 0 0 0 2 2zm6.9-2.5A2 2 0 0 0 16 16h-1v-3a1 1 0 0 0-1-1H8v-2h2a1 1 0 0 0 1-1V7h2a2 2 0 0 0 2-2v-.4a8 8 0 0 1 2.9 12.8z"/></svg>
        </li>
      </ul>
    </div>
  </section>
</main>
</body>
</html>
```